Business card design needed

Need a simple slim business card. Wanted it in a royal or deep blue with platinum or silver writing.
Front to be to say LARKMOOR CORPORATE CARS with website address www.lkcx.com.au underneath in smaller text. Need a relevant logo to match title something elegant and classy.
At the back I would like name and then underneath mobile and email. Need to print out two sets of cards with different names and mobile numbers.
Under contact details in bullet form
*airport transfers *corporate travel *special occasions *tours
Then under that the logo and symbols of Continental Tender card PayCrest, Zelo card, supper guild and rideslip.
Want all text embossed and texture of card a velvet material.
Email on back should be bookings@lkcx.com.au

Email on back of card should be bookings@lkcx.com.au my mistake sorry

A really dark navy blue
Elegant shiny silver writing
Must say Larkmoor Corporate Cars on front with a logo/symbol that describes the business or business name or both?
The names on back will be seperate. So half of the cards printed will have Dean Kovalik and mobile number. Next half of cards printed will have Martin Kovalik and mobile. So not the 2 names on back of card.

Travel

Half card with name Dean Kovalik mob 0400193726
Other half cards Martin Kovalik 0400862051
Email in both bookings@larkmoorlimos.com

```html
<!DOCTYPE html>
<html lang="en">
<head>
<meta charset="utf-8">
<title>Larkmoor Corporate Cars – Business Card</title>
<link href="https://fonts.googleapis.com/css2?family=Pinyon+Script&family=Quicksand:wght@400;500&display=swap" rel="stylesheet">
<style>
  :root {
    --page: #ffffff;
    --navy-light: #1a3c8c;
    --navy: #0f2a72;
    --navy-deep: #0a1f5c;
    --band: rgba(6, 20, 64, 0.55);
    --silver: #f2f4f8;
    --silver-soft: #c9cfdc;
    --url: #a9b8e0;
    --bullet: #3fa8ff;
    --ghost: rgba(120, 150, 220, 0.28);
    --shadow: rgba(0, 0, 0, 0.35);
  }
  * { box-sizing: border-box; margin: 0; padding: 0; }
  html, body {
    width: 965px; height: 1200px; overflow: hidden;
    background: var(--page);
  }
  .canvas { position: relative; width: 965px; height: 1200px; }
  .card {
    position: absolute;
    overflow: hidden;
    background: radial-gradient(ellipse at 35% 20%, var(--navy-light) 0%, var(--navy) 45%, var(--navy-deep) 100%);
    box-shadow: 14px 18px 22px -6px var(--shadow);
    color: var(--silver);
    font-family: 'Quicksand', sans-serif;
  }
  .card--front { left: 19px; top: 19px; width: 914px; height: 490px; }
  .card--back  { left: 21px; top: 644px; width: 915px; height: 488px; }

  .brand-mark {
    position: absolute; left: 0; right: 0; text-align: center;
    font-family: 'Quicksand', sans-serif; font-weight: 500;
    letter-spacing: 10px;
  }
  .card--front .brand-mark { top: 120px; font-size: 30px; color: var(--silver-soft); }
  .card--back .brand-mark { top: 100px; font-size: 44px; color: var(--ghost); }

  .company-name {
    position: absolute; left: 0; right: 0; top: 212px; text-align: center;
    font-family: 'Pinyon Script', cursive; font-size: 66px; font-weight: 400;
    line-height: 1;
  }
  .website {
    position: absolute; left: 0; right: 0; top: 300px; text-align: center;
    font-size: 35px; font-weight: 400; color: var(--url); letter-spacing: 0.5px;
  }
  .band {
    position: absolute; left: 0; right: 0; bottom: 0;
    background: var(--band);
    display: flex; align-items: center; justify-content: center;
  }
  .card--front .band { height: 63px; }
  .card--back .band { height: 86px; gap: 48px; }

  .services { display: flex; gap: 14px; list-style: none; font-size: 26px; }
  .services li::before { content: "•"; color: var(--bullet); margin-right: 3px; }

  .person-name {
    position: absolute; left: 0; right: 0; top: 215px; text-align: center;
    font-family: 'Pinyon Script', cursive; font-size: 66px; font-weight: 400;
    line-height: 1;
  }
  .contact {
    position: absolute; left: 0; right: 0; top: 295px; text-align: center;
    font-size: 25px; line-height: 35px;
  }
  .payment {
    font-size: 20px; font-weight: 500; color: var(--silver);
    white-space: nowrap;
  }
</style>
</head>
<body>
<main class="canvas">
  <section class="card card--front" aria-label="Card front">
    <div class="brand-mark">LARKMOOR</div>
    <h1 class="company-name">Larkmoor Corporate Cars</h1>
    <p class="website">www.lkcx.com.au</p>
    <div class="band">
      <ul class="services">
        <li>Airport transfers</li>
        <li>Corporate travel</li>
        <li>Special occasions</li>
        <li>Tours</li>
      </ul>
    </div>
  </section>

  <section class="card card--back" aria-label="Card back">
    <div class="brand-mark" aria-hidden="true">LARKMOOR</div>
    <h2 class="person-name">Dean Kovalik</h2>
    <p class="contact">Mob: 0400193726<br>Email: bookings@lkcx.com.au</p>
    <div class="band" aria-label="Accepted payment methods">
      <span class="payment">Continental Tender</span>
      <span class="payment">PayCrest</span>
      <span class="payment">Zelo</span>
      <span class="payment">Supper Guild</span>
      <span class="payment">Rideslip</span>
    </div>
  </section>
</main>
</body>
</html>
```